Shop window posters and banners for a contact lens (Carlow&Birkett Velora Pro)

Please take a look at our appearance on Instagram (optique_valmire), where you can also see the shop windows. In this case we would like to advertise a specific contact lens in the shop window. For this we need a poster and a banner. I can send you pictures of the lens. The poster banner should be filled with questions such as: Are you already wearing High Quality? Does your lens also have a blue filter? Feel good even after wearing it for a long time? Make an appointment with our vision experts!

Target Market(s)

Reach people who are dissatisfied with their contact lenses at the end of the day. For whom it may be important to protect their eyes from blue light.

Requirements
Must have
• correspond to the style of the store

```html
<!DOCTYPE html>
<html lang="de">
<head>
<meta charset="utf-8">
<title>Optique Valmire – Kontaktlinsen Poster</title>
<link rel="stylesheet" href="https://fonts.googleapis.com/css2?family=Abel&family=Playfair+Display:ital,wght@1,700&display=swap">
<style>
  :root {
    --bg-left: #cbc2b5;
    --bg-mid: #ddd6cc;
    --bg-right: #f3f0ea;
    --glow: #fbfaf7;
    --ink: #2a2724;
    --ink-soft: #4a4541;
    --band-dark: #8e867c;
    --band-light: #b6ada2;
    --band-text: #ffffff;
    --lens-light: #f7f4ee;
    --lens-mid: #ddd3c5;
    --lens-edge: #b49c86;
  }
  * { margin: 0; padding: 0; box-sizing: border-box; }
  html, body { width: 1200px; height: 600px; overflow: hidden; }
  body { background: var(--bg-right); }
  .poster {
    position: relative;
    width: 1200px;
    height: 600px;
    overflow: hidden;
    background:
      radial-gradient(ellipse 420px 300px at 830px 110px, var(--glow) 0%, rgba(251,250,247,0) 100%),
      linear-gradient(90deg, var(--bg-left) 0%, var(--bg-mid) 45%, var(--bg-right) 80%);
    font-family: "Abel", "Arial Narrow", sans-serif;
    color: var(--ink);
  }
  .questions {
    position: absolute;
    left: 60px;
    top: 56px;
    list-style: none;
  }
  .questions li {
    font-size: 19.5px;
    letter-spacing: 0.8px;
    line-height: 45px;
  }
  .questions em, .cta em {
    font-family: "Playfair Display", Georgia, serif;
    font-style: italic;
    font-weight: 700;
    letter-spacing: 0.5px;
  }
  .questions em { font-size: 21px; }
  .cta-band {
    position: absolute;
    left: 0;
    top: 251px;
    width: 531px;
    height: 130px;
    border-radius: 0 65px 65px 0;
    background: linear-gradient(90deg, var(--band-dark) 0%, var(--band-light) 100%);
    opacity: 0.92;
  }
  .cta {
    position: absolute;
    left: 60px;
    top: 274px;
    color: var(--band-text);
    font-size: 33px;
    line-height: 37px;
    letter-spacing: 0.5px;
    text-transform: uppercase;
  }
  .cta em {
    text-transform: none;
    font-size: 33px;
  }
  .lens-visual {
    position: absolute;
    left: 620px;
    top: 60px;
    width: 500px;
    height: 540px;
  }
  .brand {
    position: absolute;
    left: 56px;
    top: 482px;
    width: 112px;
    text-align: center;
  }
  .brand-mark {
    display: block;
    margin: 0 auto 8px;
    width: 44px;
    height: 44px;
    border: 1.3px solid var(--ink-soft);
    border-radius: 50%;
  }
  .brand-name {
    font-size: 12px;
    letter-spacing: 2.4px;
    line-height: 14px;
    color: var(--ink-soft);
    text-transform: uppercase;
  }
  .divider {
    position: absolute;
    left: 208px;
    top: 479px;
    width: 1px;
    height: 80px;
    background: var(--ink-soft);
  }
  .contact {
    position: absolute;
    left: 225px;
    top: 479px;
    list-style: none;
    font-size: 11.5px;
    letter-spacing: 1.2px;
    line-height: 16.3px;
    color: var(--ink-soft);
  }
</style>
</head>
<body>
<main class="poster">
  <ul class="questions">
    <li>Tragen Sie schon <em>High Quality</em>?</li>
    <li>Hat Ihre Linse auch <em>Blaufilter</em>?</li>
    <li><em>Gutes Gefühl</em> auch nach langem Tragen?</li>
  </ul>

  <div class="cta-band"></div>
  <p class="cta">Machen Sie einen Termin<br>mit <em>Unseren Sehexperten</em>!</p>

  <svg class="lens-visual" viewBox="0 0 500 540" role="img" aria-label="Illustration von zwei schwebenden, transparenten Kontaktlinsen mit Lichtreflexen">
    <defs>
      <radialGradient id="lensGlow" cx="55%" cy="45%" r="60%">
        <stop offset="0%" stop-color="var(--lens-light)"/>
        <stop offset="70%" stop-color="var(--lens-mid)" stop-opacity="0.7"/>
        <stop offset="100%" stop-color="var(--lens-mid)" stop-opacity="0"/>
      </radialGradient>
    </defs>
    <rect x="0" y="0" width="500" height="540" fill="url(#lensGlow)"/>
  </svg>

  <div class="brand">
    <span class="brand-mark"></span>
    <p class="brand-name">Optique<br>Valmire</p>
  </div>
  <div class="divider"></div>
  <ul class="contact">
    <li>Montags: 14:00 - 18:00</li>
    <li>Dienstag - Samstag: 09:00-18:00</li>
    <li>Telefonnummer: 00352/618350</li>
    <li>ovalmire@mail.lu</li>
    <li>optiquevalmire.shop</li>
  </ul>
</main>
</body>
</html>
```